Design Large Inspirational Artwork with Long Quote

Design a large piece of art with a quote from Marcus Hallwell.

QUOTE
"The thing that's so interesting about being alive is that you're all in. No matter what you do, you're all in. This is gonna kill you, so I think you might as well play the most magnificent game you can while you're waiting. Because, do you have anything better to do? Why not pick the best thing possible that you could do? Because you're more powerful than you think, way more powerful than you think. I mean, God only knows what you are in the final analysis. You're blind to your own weaknesses, but you're also blind to your own strengths. How far could you take that if you stopped wasting time, and if you stopped lying, and if you oriented yourself to the highest possible good that you could conceive of and you committed to that? How much good could you do? Well, I would say: why don't you find out?"

SIZE
A high-resolution print size of 6' wide and 3' tall should provide ample space for both the quote and the accompanying artwork.

TYPOGRAPHY
Choose a bold, clean, and easily readable font for the quote. You could also experiment with different font sizes for certain words or phrases to emphasize their importance within the quote.

COLORS
Since the quote is thought-provoking and reflective, you might want to use a color palette that evokes a sense of introspection and depth. Consider using cool, calming colors like shades of blue, gray, or green. Alternatively, you can use a contrasting color scheme with a light background and dark text to make the quote stand out.

ARTWORK
Select / create / edit background artwork to complement the quote.
While a great design might be minimalistic and/or greyscale, I'd really like to see some full color options. This might be anything from photography or graphics inspired by the ideas in the text, to abstract colors or illustrations that feel like the sentiment expressed.
The art should capture your attention and encourage you to read the text. The art should be visually appealing, both at a distance and up close, regardless of whether the text is read.
Updates

Having trouble confirming the exact print size.

Still looking for printing solution and final size confirmation.

Target Market(s)

Personal, business, office

Industry/Entity Type

None

Font styles to use
Sans Serif
Script

Requirements
Must have
• Entire quote, legible text, modern design, attractive artwork, approx 6ft wide and 3ft tall
Nice to have
• Different font (sizes) for certain words or phrases to emphasize their importance within the quote.

```html
<!DOCTYPE html>
<html lang="en">
<head>
<meta charset="utf-8">
<title>Why Don't You Find Out — Marcus Hallwell</title>
<link rel="stylesheet" href="https://fonts.googleapis.com/css2?family=Fira+Sans+Extra+Condensed:wght@300&family=Patrick+Hand&family=Pinyon+Script&display=swap">
<style>
  :root {
    --bg-dark: #2a2a2a;
    --bg-mid: #3a3a3a;
    --bg-light: #575757;
    --floor-dark: #1c1c1c;
    --floor-light: #8a8a8a;
    --frame: #ffffff;
    --text-soft: #cfcfcf;
    --text-strong: #ffffff;
  }
  * { margin: 0; padding: 0; box-sizing: border-box; }
  html, body {
    width: 1200px;
    height: 600px;
    overflow: hidden;
    background: var(--bg-dark);
  }
  .artwork {
    position: relative;
    width: 1200px;
    height: 600px;
    overflow: hidden;
    background: linear-gradient(90deg, var(--bg-dark) 0%, var(--bg-mid) 55%, var(--bg-light) 100%);
  }
  .floor {
    position: absolute;
    left: 0;
    top: 500px;
    width: 1200px;
    height: 100px;
    background:
      linear-gradient(180deg, rgba(0,0,0,0) 0%, rgba(0,0,0,0.35) 100%),
      linear-gradient(90deg, var(--floor-light) 0%, #5a5a5a 25%, var(--floor-dark) 55%, #262626 100%);
  }
  .doorway {
    position: absolute;
    left: 49px;
    top: 75px;
    width: 200px;
    height: 426px;
    border: 11px solid var(--frame);
    background: linear-gradient(180deg, #0a0a0a 0%, #6e6e6e 60%, #e8e8e8 78%, #2a2a2a 100%);
  }
  .quote {
    position: absolute;
    left: 303px;
    top: 66px;
    width: 860px;
    color: var(--text-soft);
    font-family: "Fira Sans Extra Condensed", sans-serif;
    font-weight: 300;
    font-size: 23px;
  }
  .quote-line {
    display: block;
    height: 36.7px;
    line-height: 36.7px;
    white-space: nowrap;
  }
  .quote-line--indent { padding-left: 69px; }
  .drop-cap {
    position: absolute;
    left: -16px;
    top: -14px;
    font-family: "Pinyon Script", cursive;
    font-size: 78px;
    line-height: 1;
    color: var(--text-strong);
    text-shadow: 3px 4px 4px rgba(0,0,0,0.8);
  }
  .emphasis {
    font-family: "Patrick Hand", cursive;
    font-size: 28px;
    color: var(--text-strong);
  }
  .closing {
    display: block;
    margin-top: 10px;
    font-family: "Patrick Hand", cursive;
    font-size: 40px;
    line-height: 44px;
    color: var(--text-strong);
    white-space: nowrap;
  }
</style>
</head>
<body>
<main class="artwork">
  <div class="floor" role="img" aria-label="Soft beams of light spreading across a dark floor"></div>
  <div class="doorway" role="img" aria-label="Bright open doorway with two silhouetted figures standing in the light"></div>

  <blockquote class="quote" aria-label="Quote by Marcus Hallwell">
    <span class="drop-cap" aria-hidden="true">T</span>
    <span class="quote-line quote-line--indent">he thing that’s so interesting about being alive is that you’re all in. No matter</span>
    <span class="quote-line quote-line--indent">what you do, you’re all in. This is gonna kill you, so I think you might as well</span>
    <span class="quote-line">play the most magnificent game you can while you’re waiting. <span class="emphasis">Because, do you</span></span>
    <span class="quote-line"><span class="emphasis">have anything better to do? Why not pick the best thing possible that you</span></span>
    <span class="quote-line"><span class="emphasis">could do?</span> Because you’re more powerful than you think, way more powerful than</span>
    <span class="quote-line">you think. I mean, <span class="emphasis">God</span> only knows what you are in the final analysis. You’re blind to</span>
    <span class="quote-line">your own weaknesses, but you’re also blind to your own strengths. <span class="emphasis">How far could</span></span>
    <span class="quote-line"><span class="emphasis">you take that if you stopped wasting time, and if you stopped lying, and if</span></span>
    <span class="quote-line"><span class="emphasis">you oriented yourself to the highest possible good that you could conceive</span></span>
    <span class="quote-line"><span class="emphasis">of and you committed to that? How much good could you do?</span></span>
    <span class="closing">Well, I would say: why don’t you find out?</span>
  </blockquote>
</main>
</body>
</html>
```